Soft furnishing company selling fabrics, curtains, bedlinen craft & haberdashery

We need 4 x home page banners for our website as follows:
Image 1 - to lead customers to our "New season Fabrics" page,
Image 2 - to lead customers to our Ready Made curtains,
Image 3 - to lead customers to our "Polar Bear Bed linen" page
Image 4 - to lead customers to our "Christmas raft Tutorial" page

Banner needs to be 960px wide x 380px 72dpi and optimised for web. should have a little descriptive text for example "Fabulous Fabric. Prints, plains & weaves, view our range of new season furnishing fabrics to buy by the metre" "Instantly update your home with our range of ready made curtains. Available . "Cosy Night In. Snuggle with this Polar Bear Duvet Set. From €20" "" "Let's Get Crafting for Christmas. Download our free Project and tutoirals here. First 3 images need a "shop now" button

website url www.lintelway.ie

Target Market(s)

Female 25 -45

Industry/Entity Type

It Company

Font styles to use
Serif
Sans Serif

Requirements
Must have
• shop now button on image 1, 2, 3
Should not have
• too much text or clutter

```html
<!DOCTYPE html>
<html lang="en">
<head>
<meta charset="utf-8">
<title>Christmas Craft Tutorial</title>
<link rel="stylesheet" href="https://fonts.googleapis.com/css2?family=Bodoni+Moda:opsz,wght@6..96,700&family=Ubuntu:wght@400;500&display=swap">
<style>
  :root {
    --red-bright: #ee1c24;
    --red-mid: #d10f17;
    --red-deep: #8f0709;
    --gold-light: #fbe7a6;
    --gold-mid: #e2b85a;
    --gold-deep: #c9952f;
    --white: #ffffff;
    --felt-green: #b5d68a;
    --felt-green-soft: #dcedc6;
  }
  html, body {
    margin: 0;
    padding: 0;
    overflow: hidden;
    background: var(--white);
  }
  .banner {
    position: relative;
    width: 1200px;
    height: 475px;
    overflow: hidden;
    background: var(--white);
    font-family: "Ubuntu", "Helvetica Neue", Arial, sans-serif;
  }
  .banner__shapes {
    position: absolute;
    inset: 0;
    width: 1200px;
    height: 475px;
  }
  .banner__title {
    position: absolute;
    left: 30px;
    top: 2px;
    margin: 0;
    font-family: "Bodoni Moda", "Didot", Georgia, serif;
    font-weight: 700;
    font-size: 72px;
    line-height: 72px;
    color: var(--white);
    letter-spacing: 0.5px;
  }
  .banner__text {
    position: absolute;
    left: 41px;
    top: 190px;
    margin: 0;
    font-size: 26px;
    line-height: 38px;
    color: var(--white);
  }
  .banner__button {
    position: absolute;
    left: 40px;
    top: 357px;
    width: 245px;
    height: 52px;
    box-sizing: border-box;
    border: 3px solid var(--white);
    display: flex;
    align-items: center;
    justify-content: center;
    gap: 12px;
    color: var(--white);
    text-decoration: none;
    font-weight: 500;
    font-size: 22px;
    letter-spacing: 0.2px;
  }
  .banner__button svg {
    width: 17px;
    height: 20px;
  }
</style>
</head>
<body>
  <section class="banner">
    <svg class="banner__shapes" viewBox="0 0 1200 475" aria-hidden="false">
      <defs>
        <radialGradient id="red-panel" cx="0.65" cy="0.45" r="0.8">
          <stop offset="0" stop-color="var(--red-bright)"/>
          <stop offset="0.55" stop-color="var(--red-mid)"/>
          <stop offset="1" stop-color="var(--red-deep)"/>
        </radialGradient>
        <linearGradient id="gold-band" x1="0" y1="0" x2="0" y2="1">
          <stop offset="0" stop-color="var(--gold-deep)"/>
          <stop offset="0.45" stop-color="var(--gold-mid)"/>
          <stop offset="1" stop-color="var(--gold-light)"/>
        </linearGradient>
        <radialGradient id="felt-trees" cx="0.5" cy="0.55" r="0.55">
          <stop offset="0" stop-color="var(--felt-green)"/>
          <stop offset="0.7" stop-color="var(--felt-green-soft)"/>
          <stop offset="1" stop-color="var(--white)"/>
        </radialGradient>
      </defs>
      <rect class="felt-photo" role="img" aria-label="Photo of three green felt Christmas trees with red knots, white woodland animals and red toadstools" x="650" y="10" width="545" height="445" fill="url(#felt-trees)"/>
      <path class="gold-band" d="M700 0 H768 C600 120 492 300 478 475 H462 C480 300 560 120 700 0 Z" fill="url(#gold-band)"/>
      <path class="red-panel" d="M0 0 H700 C560 120 480 300 462 475 H0 Z" fill="url(#red-panel)"/>
    </svg>

    <h1 class="banner__title">Christmas Craft<br>Tutorial</h1>
    <p class="banner__text">Let's Get Crafting for Christmas.<br>Download our free Project<br>and tutoirals here.</p>
    <a class="banner__button" href="#">VIEW TUTORIALS
      <svg viewBox="0 0 17 20" aria-hidden="true"><path d="M0 0 L17 10 L0 20 Z" fill="currentColor"/></svg>
    </a>
  </section>
</body>
</html>
```